Halcyon Glide Door Product info

Need a catalog designed. 4 -6 pages
We are a commercial sliding door company.
Primary product is a barn door
35 STC Rating (sound rating)
see our web pages listed below
www.halcyonglidedoor.example
www.quickbarsupply.example
Our product is gaining huge strides throughout the medical and hospitality sectors.
this is a 4- 6 page catalogue / brochure . Our product is currently used in many places but we also are creating new markets in the office space.
Updates

Target Market(s)

Commercial Architects , designers , Contractors .
Hospitals , high end hotels , Commercial building planners

Industry/Entity Type

Construction Company

Font styles to use
Serif

Requirements
Must have
• Selling points as to why our product is superior, good flow from concept to end. catch the eye of a designer . technical info . info on sound rating , Good photos, will provide better photos.
Nice to have
• see website from meridel doors and see ideas
Should not have
• too much writing

```html
<!DOCTYPE html>
<html lang="en">
<head>
<meta charset="utf-8">
<title>Halcyon Glide Door – Catalogue</title>
<link rel="stylesheet" href="https://fonts.googleapis.com/css2?family=Open+Sans:wght@400;600;700&family=PT+Serif:wght@400;700&display=swap">
<style>
  :root{
    --backdrop:#c4e2e4;
    --brand-blue:#1b6696;
    --brand-blue-deep:#125680;
    --accent-blue:#2a7fb3;
    --slate:#4c5f76;
    --slate-dark:#3c4c62;
    --paper:#ffffff;
    --paper-tint:#eef2f6;
    --ink:#2b3340;
    --ink-soft:#5a6472;
    --line-light:rgba(255,255,255,.75);
  }
  *{box-sizing:border-box;margin:0;padding:0}
  html,body{width:857px;height:1200px;overflow:hidden;background:var(--backdrop)}
  body{font-family:"Open Sans",Arial,sans-serif;color:var(--ink)}
  .canvas{position:relative;width:857px;height:1200px}

  .spread{position:absolute;left:28px;width:800px;height:560px;display:flex;box-shadow:0 4px 14px rgba(30,60,80,.18)}
  .spread--covers{top:30px}
  .spread--inside{top:610px}
  .page{position:relative;width:400px;height:560px;overflow:hidden}

  /* back cover */
  .back-cover{background:linear-gradient(160deg,var(--brand-blue) 0%,var(--brand-blue-deep) 100%);color:#fff;text-align:center}
  .back-cover__frame{position:absolute;border:1px solid rgba(255,255,255,.06);background:rgba(255,255,255,.03)}
  .slogan{position:absolute;left:50%;top:150px;transform:translateX(-50%);border:1px solid var(--line-light);padding:7px 16px;font-size:17px;letter-spacing:.3px;white-space:nowrap}
  .contact{position:absolute;left:0;right:0;top:212px}
  .contact__title{font-weight:700;font-size:12px;margin-bottom:16px}
  .contact__item{display:flex;flex-direction:column;align-items:center;gap:5px;font-size:10px;margin-bottom:12px}
  .contact__icon{width:14px;height:14px}
  .footer-band{position:absolute;left:0;right:0;bottom:0;height:36px;background:var(--slate-dark);color:#fff;font-size:11.5px;display:flex;align-items:center;justify-content:center;letter-spacing:.3px}
  .footer-band::before{content:"";position:absolute;left:0;right:0;top:-6px;height:6px;background:var(--accent-blue)}

  /* front cover */
  .front-cover{background:linear-gradient(180deg,var(--paper) 0%,var(--paper-tint) 100%)}
  .wordmark{position:absolute;top:48px;left:0;right:0;text-align:center;font-family:"PT Serif",Georgia,serif;color:var(--slate-dark)}
  .wordmark__name{font-size:20px;line-height:1.1}
  .wordmark__sub{font-size:11px;margin-top:3px}
  .cover-photo{position:absolute;left:46px;right:0;top:100px;height:190px;background:linear-gradient(100deg,#6d7680 0%,#a99887 45%,#7e6650 70%,#9aa0a6 100%)}
  .tagline{position:absolute;top:308px;left:0;right:0;text-align:center;font-weight:700;font-size:13px;color:var(--accent-blue);letter-spacing:.3px}
  .statement{position:absolute;top:336px;left:68px;right:36px;border:1px solid #9fb3c5;padding:5px 8px;text-align:center;color:var(--ink);font-size:13px;line-height:1.3}
  .statement__lead{font-size:14px}
  .statement__lead::before,.statement__lead::after{content:"";display:inline-block;width:80px;height:1px;background:var(--ink-soft);vertical-align:middle;margin:0 8px}
  .cover-note{position:absolute;top:392px;left:0;right:0;text-align:center;font-size:8.5px;color:var(--ink-soft)}
  .front-cover .footer-band{font-size:12px;justify-content:flex-end;padding-right:40px}

  /* inside left */
  .inside-left{background:var(--paper)}
  .feature-photo{position:absolute;left:0;right:0;top:0;height:200px;background:linear-gradient(120deg,#4b4a4d 0%,#8c7a66 35%,#b98a52 55%,#d8d3cb 80%,#9fa6ad 100%)}
  .section-head{position:absolute;top:212px;left:0;right:0;display:flex;align-items:center;gap:10px;padding:0 14px}
  .section-head__bar{flex:1;height:5px;background:var(--accent-blue)}
  .section-head__title{font-size:16px;color:var(--ink)}
  .about-text{position:absolute;top:240px;left:40px;right:30px;font-size:8.6px;line-height:1.35;text-align:center;color:var(--ink)}
  .superior-title{position:absolute;top:318px;left:0;right:0;text-align:center;font-weight:700;font-size:13px}
  .sectors{position:absolute;top:344px;left:12px;right:12px;display:grid;grid-template-columns:repeat(4,1fr);gap:6px}
  .sector__tab{background:var(--brand-blue);color:#fff;font-weight:700;font-size:9.5px;padding:4px 6px;margin-bottom:6px}
  .sector__text{font-size:7.6px;line-height:1.35;color:var(--ink)}
  .inside-left__band{position:absolute;left:0;right:0;bottom:0;height:8px;background:var(--slate)}

  /* inside right */
  .inside-right{background:var(--paper)}
  .hardware-panel{position:absolute;left:0;right:0;top:0;height:290px;background:linear-gradient(180deg,var(--slate) 0%,var(--slate-dark) 100%);color:#fff;padding:26px 22px 0 22px}
  .hardware-panel__tab{display:inline-block;background:#fff;color:var(--brand-blue);font-weight:700;font-size:13px;padding:3px 14px;border-left:5px solid var(--accent-blue)}
  .hardware-panel__lead{font-weight:700;font-size:9.5px;margin:10px 0 6px}
  .hardware-list{list-style:none;font-size:8.6px;line-height:1.45}
  .hardware-list li{display:flex;align-items:center;gap:6px}
  .hardware-list svg{width:8px;height:8px;flex:none}
  .hardware-panel__text{font-size:8.6px;line-height:1.4;margin-top:8px}
  .detail-photo{position:absolute;left:0;right:0;top:290px;bottom:0;background:linear-gradient(135deg,#d9dadb 0%,#b9bbbe 40%,#8f9296 65%,#a47a55 85%,#c9cbcd 100%)}
</style>
</head>
<body>
<main class="canvas">

  <section class="spread spread--covers">
    <article class="page back-cover">
      <div class="back-cover__frame" style="left:-40px;top:40px;width:260px;height:200px;transform:rotate(-8deg)"></div>
      <div class="back-cover__frame" style="left:180px;top:260px;width:280px;height:220px;transform:rotate(-8deg)"></div>
      <p class="slogan">Quality without compromise.</p>
      <div class="contact">
        <p class="contact__title">Contact Us:</p>
        <div class="contact__item">
          <svg class="contact__icon" viewBox="0 0 16 16"><circle cx="8" cy="8" r="7.3" fill="none" stroke="#fff"/><path d="M5.4 4.2l1.3 1.6-.7 1c.5 1.1 1.3 1.9 2.3 2.4l1-.7 1.6 1.3-.9 1.3c-2.6-.4-4.6-2.4-5-5z" fill="#fff"/></svg>
          <span>555-010-4821</span>
        </div>
        <div class="contact__item">
          <svg class="contact__icon" viewBox="0 0 16 16"><circle cx="8" cy="8" r="7.3" fill="none" stroke="#fff"/><rect x="4" y="5.2" width="8" height="5.6" fill="none" stroke="#fff"/><path d="M4 5.2l4 3 4-3" fill="none" stroke="#fff"/></svg>
          <span>sales@quickbarsupply.example</span>
        </div>
        <div class="contact__item">
          <svg class="contact__icon" viewBox="0 0 16 16"><circle cx="8" cy="8" r="7.3" fill="none" stroke="#fff"/><circle cx="8" cy="8" r="4" fill="none" stroke="#fff"/><path d="M4 8h8M8 4c-1.6 2.4-1.6 5.6 0 8M8 4c1.6 2.4 1.6 5.6 0 8" fill="none" stroke="#fff" stroke-width=".8"/></svg>
          <span>www.halcyonglidedoor.example</span>
        </div>
      </div>
      <footer class="footer-band">Copyright © Halcyon Glide Doors. All Right Reserved.</footer>
    </article>

    <article class="page front-cover">
      <div class="wordmark">
        <p class="wordmark__name">Halcyon</p>
        <p class="wordmark__sub">Glide Door Systems</p>
      </div>
      <div class="cover-photo" role="img" aria-label="Photo of a hotel corridor with glass wall and wooden sliding doors"></div>
      <p class="tagline">Sound.... Sealed.... Delivered....</p>
      <div class="statement">
        <p class="statement__lead">We are</p>
        <p>a commercial sliding door company.</p>
      </div>
      <p class="cover-note">The best performing sliding door out there, without any compromise.</p>
      <footer class="footer-band">www.halcyonglidedoor.example</footer>
    </article>
  </section>

  <section class="spread spread--inside">
    <article class="page inside-left">
      <div class="feature-photo" role="img" aria-label="Photo of a modern lobby with wooden columns and sliding door"></div>
      <div class="section-head">
        <span class="section-head__bar"></span>
        <h2 class="section-head__title">About Us</h2>
        <span class="section-head__bar"></span>
      </div>
      <p class="about-text">Our mission is to provide a space saving solution without sacrificing performance or design. Our product not only looks great, but performs! Finally there is a good solution for the faults of sliding doors! No sight lines, lever and key lockable, gasketed and even STC and NIC rated with field and lab tests! Our knowledgeable staff is ready to help address all your needs! Contact us today for inquiries.</p>
      <h3 class="superior-title">why our product is superior</h3>
      <div class="sectors">
        <div class="sector">
          <p class="sector__tab">Health Care</p>
          <p class="sector__text">Lever lockable, key lockable, or push button for privacy. Gasketed and sealed for sound, with STC and NIC ratings that keep patient rooms quiet and private.</p>
        </div>
        <div class="sector">
          <p class="sector__tab">Hospitality</p>
          <p class="sector__text">Privacy lockable and sealed from sight lines for guest suites. Our system offers a premium look and quiet operation, perfect for any hotel application.</p>
        </div>
        <div class="sector">
          <p class="sector__tab">Office Interiors</p>
          <p class="sector__text">We believe our product is a great fit for offices. Save floor space, keep meetings private and add a clean modern look to any workplace.</p>
        </div>
        <div class="sector">
          <p class="sector__tab">Home Use</p>
          <p class="sector__text">Great for use in a high end home. Quiet, sealed and easy to operate, our system fits any opening and any style of interior.</p>
        </div>
      </div>
      <div class="inside-left__band"></div>
    </article>

    <article class="page inside-right">
      <div class="hardware-panel">
        <h2 class="hardware-panel__tab">Hardware</h2>
        <p class="hardware-panel__lead">We offer a wide range of hardware to meet your specific needs:</p>
        <ul class="hardware-list">
          <li><svg viewBox="0 0 8 8"><path d="M1 4.2l2 2L7 1.6" fill="none" stroke="#fff" stroke-width="1.3"/></svg>Flush pulls</li>
          <li><svg viewBox="0 0 8 8"><path d="M1 4.2l2 2L7 1.6" fill="none" stroke="#fff" stroke-width="1.3"/></svg>Ladder pulls</li>
          <li><svg viewBox="0 0 8 8"><path d="M1 4.2l2 2L7 1.6" fill="none" stroke="#fff" stroke-width="1.3"/></svg>Custom pulls</li>
          <li><svg viewBox="0 0 8 8"><path d="M1 4.2l2 2L7 1.6" fill="none" stroke="#fff" stroke-width="1.3"/></svg>Key lockable mortise locks</li>
          <li><svg viewBox="0 0 8 8"><path d="M1 4.2l2 2L7 1.6" fill="none" stroke="#fff" stroke-width="1.3"/></svg>Thumb turn locks with or without privacy indicator</li>
          <li><svg viewBox="0 0 8 8"><path d="M1 4.2l2 2L7 1.6" fill="none" stroke="#fff" stroke-width="1.3"/></svg>Push button locks for privacy</li>
          <li><svg viewBox="0 0 8 8"><path d="M1 4.2l2 2L7 1.6" fill="none" stroke="#fff" stroke-width="1.3"/></svg>Latching, non-locking handles</li>
          <li><svg viewBox="0 0 8 8"><path d="M1 4.2l2 2L7 1.6" fill="none" stroke="#fff" stroke-width="1.3"/></svg>Auto door bottoms</li>
          <li><svg viewBox="0 0 8 8"><path d="M1 4.2l2 2L7 1.6" fill="none" stroke="#fff" stroke-width="1.3"/></svg>So much more! Tell us your application and we will find the perfect hardware for you.</li>
        </ul>
        <p class="hardware-panel__text">Our standard hardware consists of a backer plate, box track, fascia, receiving channel, felt gasketing, and a concealed floor guide. Find the handle or pull you want, or ask us to help! Our system is versatile and fully customizable. If we don't offer something for your needs, let us know and we will work with you to find the best solution.</p>
      </div>
      <div class="detail-photo" role="img" aria-label="Close-up render of the sliding door top track and rollers"></div>
    </article>
  </section>

</main>
</body>
</html>
```